Ready to eat rice packaging design

We need packaging design for pre cooked rice of different types
1. Basmati Rice
2. Brown basmati Rice
3. Jasmine Rice
4. Lemon Rice
5. Rice Pilaf
6. Biryani Rice

Back of the package will have preparation write up and Nutrition chart.

The design should have both natural as well as modern feel to it.

Examples of packages available in market enclosed.

Target Market(s)

National Food and Grocery Stores in USA

Industry/Entity Type

Grocery Store

```html
<!DOCTYPE html>
<html lang="en">
<head>
<meta charset="utf-8">
<title>Ready to Eat Brown Basmati Rice – Pouch Front</title>
<link href="https://fonts.googleapis.com/css2?family=Mr+Dafoe&family=Cinzel:wght@400;500&family=Roboto+Condensed:wght@700&family=Roboto:wght@500;700&display=swap" rel="stylesheet">
<style>
  :root {
    --backdrop: #e4e4e6;
    --pouch-pearl: #eceef6;
    --pouch-taupe: #8f8276;
    --pouch-taupe-light: #b3a79b;
    --pouch-taupe-dark: #6f6359;
    --script-white: #ffffff;
    --ribbon-brown: #8a5417;
    --ribbon-brown-light: #a86b24;
    --ribbon-text: #f6ead8;
    --badge-orange: #f2a01e;
    --badge-teal: #2b8fa3;
    --gda-neutral: #f3f3f3;
    --gda-amber: #f6a623;
    --gda-red: #e3343f;
    --gda-green: #8dc63f;
    --gda-ink: #1e1e1e;
  }
  * { margin: 0; padding: 0; box-sizing: border-box; }
  html, body {
    width: 1200px; height: 1200px; overflow: hidden;
    background: var(--backdrop);
  }
  .canvas {
    position: relative; width: 1200px; height: 1200px;
    background: radial-gradient(circle at 50% 40%, #f4f4f5 0%, var(--backdrop) 70%);
  }
  .pouch-front {
    position: absolute; left: 288px; top: 81px;
    width: 624px; height: 1038px;
    box-shadow: 0 18px 40px rgba(0,0,0,0.18);
  }
  .headline-script {
    font-family: 'Mr Dafoe', cursive;
    font-size: 128px;
    fill: var(--script-white);
  }
  .variety-name {
    font-family: 'Cinzel', serif;
    font-weight: 500;
    font-size: 38px;
    letter-spacing: 1px;
    fill: var(--ribbon-text);
  }
  .badge-number {
    font-family: 'Roboto Condensed', sans-serif;
    font-weight: 700;
    font-size: 62px;
    fill: var(--badge-teal);
  }
  .badge-unit {
    font-family: 'Roboto Condensed', sans-serif;
    font-weight: 700;
    font-size: 14px;
    fill: var(--badge-teal);
  }
  .gda-label { font-family: 'Roboto', sans-serif; font-weight: 500; font-size: 10px; fill: var(--gda-ink); }
  .gda-value { font-family: 'Roboto', sans-serif; font-weight: 700; font-size: 15px; fill: var(--gda-ink); }
  .gda-percent { font-family: 'Roboto', sans-serif; font-weight: 700; font-size: 12px; fill: var(--gda-ink); }
</style>
</head>
<body>
<div class="canvas">
  <svg class="pouch-front" viewBox="0 0 624 1038" xmlns="http://www.w3.org/2000/svg">
    <defs>
      <linearGradient id="taupe-foil" x1="0" y1="0" x2="1" y2="1">
        <stop offset="0" stop-color="var(--pouch-taupe-dark)"/>
        <stop offset="0.45" stop-color="var(--pouch-taupe)"/>
        <stop offset="0.75" stop-color="var(--pouch-taupe-light)"/>
        <stop offset="1" stop-color="var(--pouch-taupe)"/>
      </linearGradient>
      <linearGradient id="ribbon-fill" x1="0" y1="0" x2="0" y2="1">
        <stop offset="0" stop-color="var(--ribbon-brown-light)"/>
        <stop offset="1" stop-color="var(--ribbon-brown)"/>
      </linearGradient>
      <linearGradient id="rice-photo-tones" x1="0" y1="0" x2="1" y2="1">
        <stop offset="0" stop-color="#d9b88e"/>
        <stop offset="0.45" stop-color="#e6cfa8"/>
        <stop offset="0.8" stop-color="#a98a69"/>
        <stop offset="1" stop-color="#3a3532"/>
      </linearGradient>
    </defs>

    <!-- pouch body -->
    <rect class="pouch-base" x="0" y="0" width="624" height="1038" fill="url(#taupe-foil)"/>

    <!-- pearl corner sweep -->
    <path class="pearl-sweep" d="M0 0 H252 C150 40 70 150 20 300 C12 330 6 360 0 390 Z" fill="var(--pouch-pearl)"/>

    <!-- serving photo area -->
    <path class="serving-photo" role="img" aria-label="Photo of cooked brown basmati rice with egg and spring onion in a dark metal pan"
          d="M0 770 C150 700 300 640 624 570 V1038 H0 Z" fill="url(#rice-photo-tones)"/>

    <!-- headline -->
    <text class="headline-script" x="312" y="350" text-anchor="middle" transform="rotate(-4 312 330)">Ready to eat</text>

    <!-- variety ribbon -->
    <g class="variety-ribbon">
      <path d="M84 392 L610 362 L616 428 L90 458 Z" fill="url(#ribbon-fill)"/>
      <path d="M90 452 L612 422" stroke="var(--ribbon-text)" stroke-width="1.2" opacity="0.7"/>
      <text class="variety-name" x="350" y="428" text-anchor="middle" transform="rotate(-3 350 415)">BROWN BASMATI RICE</text>
    </g>

    <!-- 90 seconds badge -->
    <g class="timer-badge" transform="translate(184 640)">
      <circle r="64" fill="var(--badge-orange)"/>
      <path d="M-4 -48 A48 48 0 0 0 -46 -10" fill="none" stroke="var(--badge-teal)" stroke-width="6"/>
      <path d="M-46 10 A48 48 0 0 0 -12 46" fill="none" stroke="var(--badge-teal)" stroke-width="6"/>
      <path d="M-6 -58 L8 -48 L-6 -38 Z" fill="var(--badge-teal)"/>
      <g fill="var(--badge-teal)">
        <circle cx="16" cy="-46" r="4"/>
        <circle cx="32" cy="-36" r="4"/>
        <circle cx="43" cy="-20" r="4"/>
        <circle cx="48" cy="0" r="4"/>
        <circle cx="43" cy="20" r="4"/>
        <circle cx="32" cy="36" r="4"/>
        <circle cx="14" cy="46" r="4"/>
      </g>
      <text class="badge-number" x="-2" y="18" text-anchor="middle">90</text>
      <text class="badge-unit" x="0" y="36" text-anchor="middle">SECONDS</text>
    </g>

    <!-- front of pack nutrition -->
    <g class="nutrition-strip" transform="translate(207 948)">
      <g class="gda gda-calories">
        <rect x="0" y="0" width="46" height="66" rx="20" fill="var(--gda-neutral)"/>
        <text class="gda-label" x="23" y="14" text-anchor="middle">Calories</text>
        <text class="gda-value" x="23" y="32" text-anchor="middle">150</text>
        <ellipse cx="23" cy="50" rx="18" ry="10" fill="#fff"/>
        <text class="gda-percent" x="23" y="54" text-anchor="middle">8%</text>
      </g>
      <g class="gda gda-fat" transform="translate(49 0)">
        <rect x="0" y="0" width="46" height="66" rx="20" fill="var(--gda-amber)"/>
        <text class="gda-label" x="23" y="14" text-anchor="middle">Fat</text>
        <text class="gda-value" x="23" y="32" text-anchor="middle">8.4g</text>
        <ellipse cx="23" cy="50" rx="18" ry="10" fill="#fff"/>
        <text class="gda-percent" x="23" y="54" text-anchor="middle">12%</text>
      </g>
      <g class="gda gda-saturates" transform="translate(98 0)">
        <rect x="0" y="0" width="46" height="66" rx="20" fill="var(--gda-amber)"/>
        <text class="gda-label" x="23" y="14" text-anchor="middle">Saturates</text>
        <text class="gda-value" x="23" y="32" text-anchor="middle">2.9g</text>
        <ellipse cx="23" cy="50" rx="18" ry="10" fill="#fff"/>
        <text class="gda-percent" x="23" y="54" text-anchor="middle">15%</text>
      </g>
      <g class="gda gda-sugar" transform="translate(147 0)">
        <rect x="0" y="0" width="46" height="66" rx="20" fill="var(--gda-red)"/>
        <text class="gda-label" x="23" y="14" text-anchor="middle">Sugar</text>
        <text class="gda-value" x="23" y="32" text-anchor="middle">19.2g</text>
        <ellipse cx="23" cy="50" rx="18" ry="10" fill="#fff"/>
        <text class="gda-percent" x="23" y="54" text-anchor="middle">21%</text>
      </g>
      <g class="gda gda-salt" transform="translate(196 0)">
        <rect x="0" y="0" width="46" height="66" rx="20" fill="var(--gda-green)"/>
        <text class="gda-label" x="23" y="14" text-anchor="middle">Salt</text>
        <text class="gda-value" x="23" y="32" text-anchor="middle">0.20g</text>
        <ellipse cx="23" cy="50" rx="18" ry="10" fill="#fff"/>
        <text class="gda-percent" x="23" y="54" text-anchor="middle">3%</text>
      </g>
    </g>
  </svg>
</div>
</body>
</html>
```